New Business Card Design Project

Hi! I would like for you to design a business card for our aesthetic injections business. We offer Zelvia, filler, skin care. I would like it to be elegant, feminine, modern and sleek/clean. I like black/gold foil/ivory/parchment colors. It can be either one or two sided. I would like matte black with gold foil logo on one side and ivory with gold foil information on the other side

Target Market(s)

target market is the discerning woman who wants to look her best

Industry/Entity Type

beauty

Contact Information for Business Card

logo, name, phone, email, website, instagram, facebook, location

Requirements
Must have
• logo and info
Nice to have
• the icons for cell, instagram, email, fb etc
Should not have
• images of people

```html
<!DOCTYPE html>
<html lang="en">
<head>
<meta charset="utf-8">
<title>Velour Studio — Business Card</title>
<link href="https://fonts.googleapis.com/css2?family=Arimo:wght@400;700&display=swap" rel="stylesheet">
<style>
  :root {
    --backdrop: #2a2b2d;
    --card: #1b1c1e;
    --gold: #d9a441;
    --gold-deep: #b9822a;
    --glyph: #1b1c1e;
  }
  * { margin: 0; padding: 0; box-sizing: border-box; }
  html, body {
    width: 1200px; height: 1108px; overflow: hidden;
    background: var(--backdrop);
    font-family: "Arimo", Arial, sans-serif;
  }
  .canvas {
    position: relative; width: 1200px; height: 1108px;
    display: flex; justify-content: center; align-items: center; gap: 60px;
  }
  .card {
    width: 420px; height: 680px;
    background: var(--card);
    border-radius: 24px;
    box-shadow: 0 14px 40px rgba(0,0,0,.45);
    display: flex; flex-direction: column; align-items: center;
    color: var(--gold);
    overflow: hidden;
  }
  .card--front { padding-top: 40px; }
  .card--back { justify-content: center; }
  .brand-seal {
    flex: 0 0 auto;
    width: 270px; height: 270px; border-radius: 50%;
    border: 2px solid var(--gold);
    display: flex; align-items: center; justify-content: center;
    text-align: center;
  }
  .brand-name {
    font-weight: 400; font-size: 32px; line-height: 1.35;
    letter-spacing: 6px; color: var(--gold);
  }
  .holder { margin-top: 26px; text-align: center; }
  .holder__name { font-weight: 700; font-size: 22px; line-height: 26px; letter-spacing: .5px; }
  .holder__role { font-size: 17px; line-height: 20px; }
  .icon-rule {
    display: flex; align-items: center; gap: 6px; margin-top: 14px;
  }
  .icon-rule__line { width: 50px; height: 2px; background: var(--gold); }
  .icon-rule__line--left { margin-right: 6px; }
  .icon-rule__line--right { margin-left: 6px; }
  .icon { width: 24px; height: 24px; display: block; flex: 0 0 auto; }
  .contacts { margin-top: 14px; text-align: center; font-size: 19px; line-height: 25px; }
  .divider { flex: 0 0 auto; width: 280px; height: 2px; background: var(--gold-deep); margin-top: 20px; }
  .address { margin-top: 16px; text-align: center; font-size: 19px; line-height: 25px; font-style: normal; }
</style>
</head>
<body>
<main class="canvas">
  <section class="card card--front">
    <div class="brand-seal"><span class="brand-name">VELOUR<br>STUDIO</span></div>

    <div class="holder">
      <p class="holder__name">MARCUS HALE</p>
      <p class="holder__role">Manager</p>
    </div>

    <div class="icon-rule">
      <span class="icon-rule__line icon-rule__line--left"></span>
      <svg class="icon" viewBox="0 0 24 24" aria-label="phone">
        <circle cx="12" cy="12" r="12" fill="var(--gold)"/>
        <path d="M8.5 6.5l2 2-1 1.5c.8 1.6 2 2.8 3.5 3.5l1.5-1 2 2-1.5 2c-3.8-.4-7.6-4.2-8-8z" fill="var(--glyph)"/>
      </svg>
      <svg class="icon" viewBox="0 0 24 24" aria-label="email">
        <circle cx="12" cy="12" r="12" fill="var(--gold)"/>
        <rect x="6" y="8" width="12" height="8.5" rx="1" fill="none" stroke="var(--glyph)" stroke-width="1.6"/>
        <path d="M6.5 8.5l5.5 4.5 5.5-4.5" fill="none" stroke="var(--glyph)" stroke-width="1.6"/>
      </svg>
      <svg class="icon" viewBox="0 0 24 24" aria-label="website">
        <circle cx="12" cy="12" r="12" fill="var(--gold)"/>
        <circle cx="12" cy="12" r="6" fill="none" stroke="var(--glyph)" stroke-width="1.5"/>
        <ellipse cx="12" cy="12" rx="2.6" ry="6" fill="none" stroke="var(--glyph)" stroke-width="1.3"/>
        <path d="M6 12h12" stroke="var(--glyph)" stroke-width="1.3"/>
      </svg>
      <svg class="icon" viewBox="0 0 24 24" aria-label="share">
        <circle cx="12" cy="12" r="12" fill="var(--gold)"/>
        <path d="M15.5 8L8.5 12l7 4" fill="none" stroke="var(--glyph)" stroke-width="1.5"/>
        <circle cx="15.5" cy="8" r="2" fill="var(--glyph)"/>
        <circle cx="8.5" cy="12" r="2" fill="var(--glyph)"/>
        <circle cx="15.5" cy="16" r="2" fill="var(--glyph)"/>
      </svg>
      <svg class="icon" viewBox="0 0 24 24" aria-label="location">
        <circle cx="12" cy="12" r="12" fill="var(--gold)"/>
        <path d="M12 18.5s-4.5-4.6-4.5-7.8a4.5 4.5 0 0 1 9 0c0 3.2-4.5 7.8-4.5 7.8z" fill="var(--glyph)"/>
        <circle cx="12" cy="10.7" r="1.7" fill="var(--gold)"/>
      </svg>
      <span class="icon-rule__line icon-rule__line--right"></span>
    </div>

    <div class="contacts">
      <p>555-014-2187</p>
      <p>hello@velourstudio.co</p>
      <p>www.velourstudio.co</p>
      <p>velourskin.co</p>
      <p>velourskin.co</p>
    </div>

    <div class="divider"></div>

    <address class="address">
      <p>48 Linden Row, Marlow</p>
      <p>state, ZIP 0417</p>
    </address>
  </section>

  <section class="card card--back">
    <div class="brand-seal"><span class="brand-name">VELOUR<br>STUDIO</span></div>
  </section>
</main>
</body>
</html>
```